Business / Discount Card

Looking to create a 2 sided business card. Front side to say "Thanks for flying with Skyward Drifts" then have link to "In-Flight Photos, www.skywarddrifts-example.com.au, password: skyward" Back side of card to have company logo, phone number, facebook & instagram logo and #skywarddrifts. Also included on this side will be discount text "Book again and save 10%. Use discount code: skyward10"Round Corner Card Templates are attached. Please ensure dimensions are correct.Thanks,

Font styles to use
Sans Serif

Colors
33a6d7
ffffff
000000

Requirements
Must have
• Logo
• Blue, White and Black color scheme

```html
<!DOCTYPE html>
<html lang="en">
<head>
<meta charset="utf-8">
<title>Skyward Drifts – Discount Card</title>
<link rel="stylesheet" href="https://fonts.googleapis.com/css2?family=Lato:ital,wght@0,400;0,700;1,400&family=Open+Sans:wght@400;700&family=Oswald:wght@500&display=swap">
<style>
  :root {
    --sky: #00aeef;
    --white: #ffffff;
    --black: #000000;
    --backdrop: #8c8c8c;
    --ink: #222222;
  }
  html, body {
    margin: 0;
    padding: 0;
    width: 1200px;
    height: 1200px;
    overflow: hidden;
    background: var(--backdrop);
  }
  .canvas {
    position: relative;
    width: 1200px;
    height: 1200px;
  }
  .card {
    position: absolute;
    top: 310px;
    height: 594px;
    overflow: hidden;
    box-shadow: 2px 3px 6px rgba(0,0,0,0.45);
  }
  .card-back { left: 234px; width: 364px; background: var(--white); }
  .card-front { left: 627px; width: 369px; background: var(--sky); }

  .card-shapes { position: absolute; inset: 0; }

  .brand {
    position: absolute;
    top: 118px;
    left: 0;
    width: 100%;
    text-align: center;
    font-family: "Open Sans", sans-serif;
    font-weight: 700;
    font-size: 38px;
    line-height: 1;
    color: var(--sky);
  }
  .brand-mark {
    display: inline-block;
    width: 16px;
    height: 16px;
    border-radius: 50%;
    background: var(--black);
    vertical-align: middle;
    margin-right: 10px;
  }
  .phone {
    position: absolute;
    top: 327px;
    left: 0;
    width: 100%;
    text-align: center;
    font-family: "Oswald", sans-serif;
    font-weight: 500;
    font-size: 32px;
    line-height: 42px;
    color: var(--white);
    padding-left: 40px;
    box-sizing: border-box;
  }
  .social {
    position: absolute;
    top: 408px;
    left: 0;
    width: 100%;
    display: flex;
    justify-content: center;
    gap: 4px;
  }
  .social-dot {
    width: 27px;
    height: 27px;
    border-radius: 50%;
    background: #3b5998;
  }
  .hashtag {
    position: absolute;
    top: 442px;
    left: 0;
    width: 100%;
    text-align: center;
    font-family: "Open Sans", sans-serif;
    font-size: 20px;
    color: var(--ink);
  }
  .discount {
    position: absolute;
    top: 505px;
    left: 0;
    width: 100%;
    text-align: center;
    font-family: "Open Sans", sans-serif;
    font-size: 19px;
    line-height: 31px;
    color: var(--white);
  }
  .discount-code {
    font-family: "Oswald", sans-serif;
    font-weight: 500;
    font-size: 24px;
    color: var(--sky);
  }

  .front-top { position: absolute; left: 0; top: 0; width: 100%; height: 150px; background: var(--black); }
  .balloon-art {
    position: absolute;
    left: 0;
    top: 0;
    width: 369px;
    height: 400px;
    border-radius: 0 0 50% 50% / 0 0 40% 40%;
    background: radial-gradient(ellipse at 50% 40%, #ffffff 0%, #bfe9fb 45%, var(--sky) 100%);
  }
  .thanks {
    position: absolute;
    top: 411px;
    left: 0;
    width: 100%;
    text-align: center;
    font-family: "Lato", sans-serif;
    font-weight: 700;
    font-size: 20px;
    line-height: 24px;
    color: var(--white);
  }
  .photo-access {
    position: absolute;
    top: 501px;
    left: 0;
    width: 100%;
    text-align: center;
    font-family: "Lato", sans-serif;
    color: var(--white);
  }
  .photo-label { font-size: 17px; line-height: 22px; }
  .photo-url { font-size: 19px; line-height: 25px; }
  .photo-password { font-size: 16px; line-height: 20px; font-style: italic; }
</style>
</head>
<body>
<main class="canvas">

  <section class="card card-back" aria-label="Card side with contact details">
    <svg class="card-shapes" width="364" height="594" viewBox="0 0 364 594" aria-hidden="true">
      <path d="M0 322 Q182 300 364 322 L364 380 Q182 366 0 380 Z" fill="var(--sky)"/>
      <path d="M0 477 Q182 492 364 477 L364 594 L0 594 Z" fill="var(--black)"/>
    </svg>
    <div class="brand"><span class="brand-mark"></span>Skyward Drifts</div>
    <div class="phone">044-987 654 321</div>
    <div class="social" aria-label="Social media">
      <span class="social-dot"></span>
      <span class="social-dot"></span>
    </div>
    <div class="hashtag">#skywarddrifts</div>
    <div class="discount">
      Book again and save 10%.<br>
      Use discount code: <span class="discount-code">SKYWARD10</span>
    </div>
  </section>

  <section class="card card-front" aria-label="Card side with thank-you message">
    <div class="front-top"></div>
    <div class="balloon-art" role="img" aria-label="Large striped hot air balloon illustration in blue and white"></div>
    <div class="thanks">THANKS FOR FLYING WITH<br>SKYWARD DRIFTS</div>
    <div class="photo-access">
      <div class="photo-label">In-Flight Photo</div>
      <div class="photo-url">www.skywarddrifts-example.com.au</div>
      <div class="photo-password">password: skyward</div>
    </div>
  </section>

</main>
</body>
</html>
```